TRV Business Card

Business card design for a handyman company. Want to portray a professional image and stay away from the "Mom & Pops" image that is normally associated with handyman companies.

Business

```html
<!DOCTYPE html>
<html lang="en">
<head>
<meta charset="utf-8">
<title>TRV Business Card</title>
<link rel="stylesheet" href="https://fonts.googleapis.com/css2?family=Open+Sans:wght@400;600;700&family=Arimo:wght@400&display=swap">
<style>
  :root {
    --navy: #0e2140;
    --grey: #959595;
    --grey-dark: #8a8a8a;
    --white: #ffffff;
    --muted: #8f97a6;
    --ink: #111111;
    --backdrop: #e9e7e4;
  }
  * { box-sizing: border-box; margin: 0; padding: 0; }
  html, body { width: 1200px; height: 786px; overflow: hidden; }
  body {
    background: var(--backdrop);
    position: relative;
    font-family: "Open Sans", Arial, sans-serif;
  }
  .card {
    position: absolute;
    width: 520px;
    height: 300px;
    overflow: hidden;
    box-shadow: 0 6px 16px rgba(0,0,0,0.25);
  }
  .card--contact { left: 50px; top: 60px; background: var(--white); }
  .card--navy { left: 630px; top: 60px; background: var(--navy); }
  .card--grey { left: 340px; top: 430px; background: var(--grey-dark); }

  .card__curve { position: absolute; inset: 0; }

  .wordmark {
    font-family: "Open Sans", Arial, sans-serif;
    font-weight: 700;
    letter-spacing: 4px;
    line-height: 1;
  }
  .card--contact .wordmark {
    position: absolute; left: 52px; top: 118px;
    font-size: 64px; color: var(--navy);
  }

  .contact {
    position: absolute; right: 26px; top: 30px;
    text-align: right; color: var(--white);
    font-size: 15px; line-height: 1.35;
  }
  .contact__name { color: var(--ink); font-weight: 700; font-size: 19px; }
  .contact__title { color: var(--ink); font-size: 16px; margin-bottom: 26px; }
  .contact__phones { font-size: 16px; margin-bottom: 30px; }
  .contact__address { margin-bottom: 14px; }
  .contact__row { display: flex; justify-content: flex-end; align-items: center; gap: 4px; }
  .contact__row svg { width: 13px; height: 13px; }

  .promo { text-align: center; }
  .promo .wordmark { font-size: 72px; margin-top: 42px; }
  .card--navy .wordmark { color: var(--white); }
  .card--grey .wordmark { color: var(--white); }
  .services {
    font-family: "Arimo", Arial, sans-serif;
    font-size: 17px; line-height: 1.3;
    margin-top: 40px;
  }
  .card--navy .services { color: var(--muted); }
  .card--grey .services { color: var(--white); }
  .website {
    font-size: 14px; letter-spacing: 2px;
    color: var(--white); margin-top: 16px;
  }
</style>
</head>
<body>

  <section class="card card--contact" aria-label="Business card front">
    <svg class="card__curve" viewBox="0 0 520 300" preserveAspectRatio="none" aria-hidden="true">
      <path d="M262 0 Q330 150 300 300 L520 300 L520 0 Z" fill="var(--grey)"/>
      <path d="M242 0 Q312 150 282 300" fill="none" stroke="var(--navy)" stroke-width="7"/>
    </svg>
    <div class="wordmark">TRV</div>
    <div class="contact">
      <div class="contact__name">Your Name</div>
      <div class="contact__title">Title</div>
      <div class="contact__phones">
        <div class="contact__row">
          <svg viewBox="0 0 16 16"><path d="M4 1l3 3-2 2c1 2 3 4 5 5l2-2 3 3-2 3C7 15 1 9 1 3z" fill="none" stroke="#fff" stroke-width="1.4"/></svg>555-014-2290
        </div>
        <div class="contact__row">
          <svg viewBox="0 0 16 16"><rect x="4" y="1" width="8" height="5" fill="#fff"/><rect x="1" y="6" width="14" height="7" rx="1" fill="#fff"/></svg>555-014-7731
        </div>
      </div>
      <div class="contact__address">2417 Harlan Ave.<br>Westbrook, KS 66000</div>
      <div class="contact__row">
        <svg viewBox="0 0 16 16"><rect x="1" y="3" width="14" height="10" fill="#fff"/><path d="M1 3l7 6 7-6" fill="none" stroke="var(--grey)" stroke-width="1.3"/></svg>info@TRVservices.com
      </div>
    </div>
  </section>

  <section class="card card--navy promo" aria-label="Business card back, navy">
    <div class="wordmark">TRV</div>
    <div class="services">
      Residential &amp; Commercial Services &nbsp; • Potential Verbage<br>
      • Home Repairs &nbsp; • Handyman Services<br>
      • Drain Cleaning &nbsp; • Carpet Cleaning
    </div>
    <div class="website">www.trvservices.com</div>
  </section>

  <section class="card card--grey promo" aria-label="Business card back, grey">
    <div class="wordmark">TRV</div>
    <div class="services">
      Residential &amp; Commercial Services &nbsp; • Potential Verbage<br>
      • Home Repairs &nbsp; • Handyman Services<br>
      • Drain Cleaning &nbsp; • Carpet Cleaning
    </div>
    <div class="website">www.trvservices.com</div>
  </section>

</body>
</html>
```